WordPress Site That Reviews Footwear

We need a wordpress web design for an affiliate site called TreadNest. We review and do roundups on footwear products. The final design should be clean and mobile friendly. The site should be built with Gutenberg page builder. We like the design of https://dermalquill.com/.
Updates

Need extra days to review

Target Market(s)

USA

Industry/Entity Type

Footwear

Logo Text

TreadNest

Number of Pages Required

4 page

Font styles to use
Serif
Sans Serif

Requirements
Must have
• Wordpress site
Blog post
Page
Categories
Homepage

```html
<!DOCTYPE html>
<html lang="en">
<head>
<meta charset="utf-8">
<title>TreadNest — Footwear For Everyone</title>
<link href="https://fonts.googleapis.com/css2?family=Playfair+Display:wght@400;700;900&family=Poppins:wght@400;500;600&display=swap" rel="stylesheet">
<style>
:root{
  --ink:#1c1c1c;
  --text:#444;
  --muted:#777;
  --accent:#d8262c;
  --panel:#f3f3f3;
  --slate:#537887;
  --white:#fff;
  --footer:#f4f4f4;
  --line:#dcdcdc;
  --icon-tone:#e6e6e6;
}
*{margin:0;padding:0;box-sizing:border-box}
html,body{width:1200px;height:3180px;overflow:hidden;background:var(--white)}
body{position:relative;font-family:'Poppins',sans-serif;color:var(--ink)}
.abs{position:absolute}
h1,h2,h3,h4,h5{font-weight:400}

/* header */
.hero-panel{left:594px;top:0;width:606px;height:632px;background:var(--panel)}
.nav{top:38px;font-size:12px;font-weight:500;letter-spacing:.2px;display:flex;gap:24px;text-transform:uppercase}
.nav-left{left:88px}
.nav-right{left:817px}
.caret{font-size:8px;margin-left:2px}
.brand{left:0;width:1200px;top:24px;text-align:center;font-family:'Playfair Display',serif;font-size:33px;font-weight:400}
.brand b{font-weight:700}
.icons{left:1013px;top:34px;display:flex;gap:16px}
.cart-badge{left:1095px;top:30px;width:14px;height:14px;border-radius:50%;background:var(--accent);color:#fff;font-size:8px;text-align:center;line-height:14px}

/* hero */
.hero-title{left:86px;top:200px;font-family:'Playfair Display',serif;font-size:60px;line-height:58px;font-weight:400}
.hero-title b{font-weight:900}
.hero-copy{left:88px;top:392px;width:440px;font-size:14px;line-height:20px;color:var(--text)}
.hero-link{left:88px;top:459px;font-size:13px;font-weight:600;text-transform:uppercase;border-bottom:1px solid var(--ink);padding-bottom:2px}
.hero-arrow{left:376px;top:462px}
.hero-shoe{left:420px;top:467px;width:380px;height:232px;border-radius:50% 50% 45% 45%;background:radial-gradient(ellipse at 45% 45%,#d98a45,#b8652a 60%,rgba(255,255,255,0) 72%)}
.cats{left:683px;top:183px;display:grid;grid-template-columns:repeat(3,135px);gap:12px 12px}
.cat{height:126px;background:var(--white);box-shadow:0 6px 18px rgba(0,0,0,.06);display:flex;flex-direction:column;align-items:center;justify-content:flex-end;padding-bottom:22px;font-size:14px;font-weight:500;gap:18px}
.cat-icon{width:74px;height:36px;border-radius:6px;background:var(--icon-tone)}

/* section headings */
.sec-title{left:0;width:1200px;text-align:center;font-family:'Playfair Display',serif;font-size:34px;font-weight:400}
.sec-title b{font-weight:700}
.sec-rule{left:585px;width:30px;height:2px;background:var(--accent)}
.sec-copy{left:0;width:1200px;text-align:center;font-size:14px;color:var(--text)}

/* product band */
.band{left:0;top:917px;width:898px;height:578px;background:var(--slate)}
.band-circle{left:685px;top:995px;width:422px;height:422px;border-radius:50%;background:var(--panel)}
.band-shoe{left:725px;top:1070px;width:340px;height:270px;border-radius:40%;background:radial-gradient(ellipse at center,#d9ad3c,#c2922a 55%,rgba(243,243,243,0) 72%)}
.prod-name{left:87px;top:1012px;color:#fff;font-family:'Playfair Display',serif;font-size:32px;font-weight:400}
.prod-sub{left:87px;top:1054px;color:#fff;font-family:'Playfair Display',serif;font-size:14px}
.prod-rule{left:88px;top:1083px;width:30px;height:2px;background:#fff}
.prod-price{left:84px;top:1092px;color:#fff;font-family:'Playfair Display',serif;font-size:70px;font-weight:700}
.prod-copy{left:88px;top:1191px;width:460px;color:#fff;font-size:14px;line-height:19.5px}
.swatches{left:88px;top:1290px;display:flex;gap:8px}
.swatch{width:25px;height:25px;border-radius:50%}
.btn{left:88px;top:1346px;width:193px;height:42px;background:#fff;color:var(--ink);font-size:13px;font-weight:600;text-align:center;line-height:42px}

/* advice */
.advice-shoe{left:358px;top:1747px;width:470px;height:310px;border-radius:60% 40% 45% 35%;background:radial-gradient(ellipse at 50% 50%,#d42020,#b51414 60%,rgba(255,255,255,0) 72%)}
.feat{font-size:14px;font-weight:500;text-align:center;line-height:17px;width:160px}
.side-photo{left:0;top:2099px;width:173px;height:166px;background:linear-gradient(135deg,#9a6038,#e8e2dc);border-radius:0 40% 40% 0}
.divider{left:88px;top:2158px;width:1023px;height:1px;background:var(--line)}

/* blog */
.card{top:2351px;width:246px;height:334px;background:#fff;box-shadow:0 8px 24px rgba(0,0,0,.06)}
.card-img{height:175px}
.card-meta{margin:28px 0 0 21px;font-size:10.5px;color:var(--muted)}
.card-title{margin:6px 21px 0;font-family:'Playfair Display',serif;font-size:19px;line-height:21px;font-weight:400}
.card-copy{margin:10px 21px 0;font-size:12px;line-height:18px;color:var(--text)}

/* footer */
.footer{left:0;top:2780px;width:1200px;height:400px;background:var(--footer)}
.f-head{top:2846px;font-family:'Playfair Display',serif;font-size:18px;font-weight:700;color:#333}
.f-links{top:2888px;font-size:13px;line-height:26.8px;color:#333;list-style:none}
.f-contact{left:589px;top:2888px;font-size:13px;line-height:19px;color:#333}
.f-contact div{display:flex;gap:10px;margin-bottom:11px}
.socials{left:849px;top:2890px;display:flex;gap:8px}
.social{width:31px;height:31px;border-radius:50%}
.pays{left:860px;top:2998px;display:flex;gap:10px}
.pay{width:49px;height:31px;border-radius:6px}
.f-rule{left:92px;top:3116px;width:1019px;height:1px;background:#ccc}
.copy{left:0;width:1200px;top:3144px;text-align:center;font-size:13px;font-weight:500}
.top-btn{left:1134px;top:3106px;width:40px;height:40px;border-radius:50%;background:var(--accent);display:flex;align-items:center;justify-content:center}
</style>
</head>
<body>

<div class="abs hero-panel"></div>

<nav class="abs nav nav-left">
  <span>Men<span class="caret">&#8964;</span></span>
  <span>Women<span class="caret">&#8964;</span></span>
  <span>Kids<span class="caret">&#8964;</span></span>
  <span>Favorites</span>
  <span>Customize</span>
</nav>
<div class="abs brand">Tread<b>Nest</b></div>
<nav class="abs nav nav-right"><span>About</span><span>Contact Us</span></nav>
<div class="abs icons">
  <svg width="20" height="22" viewBox="0 0 20 22" fill="none" stroke="#222" stroke-width="1.6"><circle cx="10" cy="7" r="5"/><path d="M2 21c0-5 4-8 8-8s8 3 8 8"/></svg>
  <svg width="20" height="22" viewBox="0 0 20 22" fill="none" stroke="#222" stroke-width="1.6"><circle cx="8.5" cy="9" r="6.5"/><path d="M13.5 14l5 5"/></svg>
  <svg width="22" height="22" viewBox="0 0 22 22" fill="none" stroke="#222" stroke-width="1.6"><path d="M1 3h3l3 11h11l2-8H6"/><circle cx="8" cy="19" r="1.5"/><circle cx="17" cy="19" r="1.5"/></svg>
</div>
<div class="abs cart-badge">0</div>

<h1 class="abs hero-title">Footwear<br>For <b>Everyone</b><br>TreadNest</h1>
<p class="abs hero-copy">Aenean sollicitudin, lorem quis bibendum auctor amet nibh vulputate cursus a sit amet mauris morbi...</p>
<a class="abs hero-link">Check out a few of our favorites</a>
<svg class="abs hero-arrow" width="64" height="34" viewBox="0 0 64 34" fill="none" stroke="#d8262c" stroke-width="1.4"><path d="M2 4c10 20 34 30 56 10"/><path d="M50 10l8 4 1-8"/></svg>
<div class="abs hero-shoe" role="img" aria-label="Pair of tan leather sandal-shoes"></div>

<div class="abs cats">
  <div class="cat"><div class="cat-icon" role="img" aria-label="Line illustration of a sandal"></div>Sandals</div>
  <div class="cat"><div class="cat-icon" role="img" aria-label="Line illustration of a shoe"></div>Shoes</div>
  <div class="cat"><div class="cat-icon" role="img" aria-label="Line illustration of a flat"></div>Flats</div>
  <div class="cat"><div class="cat-icon" role="img" aria-label="Line illustration of a heel"></div>Heels</div>
  <div class="cat"><div class="cat-icon" role="img" aria-label="Line illustration of an ethnic sandal"></div>Ethnic</div>
  <div class="cat"><div class="cat-icon" role="img" aria-label="Line illustration of a slipper"></div>Slippers</div>
</div>

<h2 class="abs sec-title" style="top:782px">What’s Your Tread<b>Nest</b></h2>
<div class="abs sec-rule" style="top:830px"></div>
<p class="abs sec-copy" style="top:843px">Aenean sollicitudin lorem quis bibendum auctor amet nibh vulputate cursus a sit amet mauris morbi...</p>

<section>
  <div class="abs band"></div>
  <div class="abs band-circle"></div>
  <div class="abs band-shoe" role="img" aria-label="Pair of mustard leather lace-up boots"></div>
  <h3 class="abs prod-name">Stride Aero Knit 2</h3>
  <p class="abs prod-sub">Incredibly Comfortable Footware</p>
  <div class="abs prod-rule"></div>
  <div class="abs prod-price">$100</div>
  <p class="abs prod-copy">Aenean sollicitudin lorem quis biendum auctor nisi elit cumsan ipsum velit. Nam nec tellus a odio tincidunt auctor a odio. Sed non mauris vitae erat consequat auctor eu in elit aptent tacitis sociosqu ad litora torquent per conubia...</p>
  <div class="abs swatches">
    <span class="swatch" style="background:#fff"></span>
    <span class="swatch" style="background:#4fd0f2"></span>
    <span class="swatch" style="background:#e4b03c;box-shadow:inset 0 0 0 9px #e4b03c,inset 0 0 0 12px #fff"></span>
    <span class="swatch" style="background:#5fd47a"></span>
  </div>
  <a class="abs btn">CHECK OUT A FEW</a>
</section>

<h2 class="abs sec-title" style="top:1573px">Finally... TreadNest <b>Advice</b></h2>
<div class="abs sec-rule" style="top:1620px"></div>
<p class="abs sec-copy" style="top:1634px">Aenean sollicitudin lorem quis bibendum auctor amet nibh vulputate cursus a sit amet mauris morbi...</p>

<div class="abs advice-shoe" role="img" aria-label="Red knit running shoe"></div>
<svg class="abs" style="left:0;top:1700px" width="1200" height="400" viewBox="0 1700 1200 400" fill="none">
  <g stroke="#9a9a9a" stroke-width="1" stroke-dasharray="4 4">
    <path d="M240 1767c30 40 100 40 154 26"/>
    <path d="M749 1769c-30 40-90 50-159 33"/>
    <path d="M933 1862c-60 40-160 30-266 15"/>
    <path d="M349 1935c40 40 140 30 207-5"/>
    <path d="M942 1972c-40 30-120 30-185-13"/>
    <path d="M467 2046c60 40 160 20 222-50"/>
  </g>
  <g fill="#999" stroke="#fff" stroke-width="2">
    <circle cx="240" cy="1767" r="5"/><circle cx="394" cy="1793" r="5"/>
    <circle cx="749" cy="1769" r="5"/><circle cx="590" cy="1802" r="5"/>
    <circle cx="933" cy="1862" r="5"/><circle cx="667" cy="1877" r="5"/>
    <circle cx="349" cy="1935" r="5"/><circle cx="556" cy="1930" r="5"/>
    <circle cx="942" cy="1972" r="5"/><circle cx="757" cy="1959" r="5"/>
    <circle cx="467" cy="2046" r="5"/><circle cx="689" cy="1996" r="5"/>
  </g>
</svg>
<div class="abs feat" style="left:160px;top:1716px">Light Weight<br>Material</div>
<div class="abs feat" style="left:693px;top:1716px">Adjustable Lacing<br>System</div>
<div class="abs feat" style="left:850px;top:1811px">Natural Fitting<br>Comfort</div>
<div class="abs feat" style="left:232px;top:1903px">Strong Midsole</div>
<div class="abs feat" style="left:861px;top:1919px">Integral Support<br>Straps</div>
<div class="abs feat" style="left:383px;top:1997px">Antioodor Molded<br>Footbeb</div>

<div class="abs side-photo" role="img" aria-label="Brown and white strap sandal"></div>
<div class="abs divider"></div>

<h2 class="abs sec-title" style="top:2236px">Learn From The <b>Experts.</b></h2>
<div class="abs sec-rule" style="top:2284px"></div>
<p class="abs sec-copy" style="top:2297px">Aenean sollicitudin lorem quis bibendum auctor amet nibh vulputate cursus a sit amet mauris morbi...</p>

<article class="abs card" style="left:214px">
  <div class="card-img" style="background:#f6c6c9" role="img" aria-label="Pink and white heeled sandals on a pink backdrop"></div>
  <p class="card-meta">By John &nbsp;•&nbsp; January 2021</p>
  <h4 class="card-title">Some blog heading<br>goes here</h4>
  <p class="card-copy">Nisi elit consequat ipsum nec sagittis sem nibh id elit....</p>
</article>
<article class="abs card" style="left:478px">
  <div class="card-img" style="background:#dcdcdc" role="img" aria-label="White sneakers on a grey backdrop"></div>
  <p class="card-meta">By John &nbsp;•&nbsp; January 2021</p>
  <h4 class="card-title">Some blog heading<br>goes here</h4>
  <p class="card-copy">Nisi elit consequat ipsum nec sagittis sem nibh id elit....</p>
</article>
<article class="abs card" style="left:741px">
  <div class="card-img" style="background:#f5dcbc" role="img" aria-label="Black heeled pumps on a beige backdrop"></div>
  <p class="card-meta">By John &nbsp;•&nbsp; January 2021</p>
  <h4 class="card-title">Some blog heading<br>goes here</h4>
  <p class="card-copy">Nisi elit consequat ipsum nec sagittis sem nibh id elit....</p>
</article>

<footer>
  <div class="abs footer"></div>
  <h5 class="abs f-head" style="left:128px">Let us help you</h5>
  <ul class="abs f-links" style="left:129px"><li>Search</li><li>About Us</li><li>Footwear Size</li><li>Care Guide</li><li>Shipping</li><li>Contact</li><li>FAQS</li></ul>
  <h5 class="abs f-head" style="left:365px">Information</h5>
  <ul class="abs f-links" style="left:365px"><li>Site Map</li><li>Terms &amp; Condition</li><li>Privacy Policy</li><li>FAQ's</li><li>Customer Service</li><li>Disclaimer</li></ul>
  <h5 class="abs f-head" style="left:589px">Contact Us</h5>
  <div class="abs f-contact">
    <div><svg width="13" height="13" viewBox="0 0 13 13"><rect x="0" y="2" width="13" height="9" fill="#d8262c"/><path d="M0 2l6.5 5L13 2" stroke="#fff" fill="none"/></svg><span>Email:<br>hello@treadnest-mail.com</span></div>
    <div><svg width="13" height="13" viewBox="0 0 13 13" fill="none" stroke="#d8262c" stroke-width="1.6"><path d="M2 1l3 3-1.5 2a8 8 0 0 0 3.5 3.5L9 8l3 3-2 2C5 12 1 8 0 3z"/></svg><span>Phone:<br>(+01) 555 014 2236</span></div>
    <div><svg width="13" height="15" viewBox="0 0 13 15"><path d="M6.5 0A5 5 0 0 0 1.5 5c0 4 5 10 5 10s5-6 5-10a5 5 0 0 0-5-5z" fill="#d8262c"/><circle cx="6.5" cy="5" r="2" fill="#fff"/></svg><span>Office Location:<br>48 Cobbler Lane, Suite 5<br>Millbrook</span></div>
  </div>
  <h5 class="abs f-head" style="left:849px">Stay Connected</h5>
  <div class="abs socials"><span class="social" style="background:#3b5998"></span><span class="social" style="background:#1da1f2"></span><span class="social" style="background:#c13584"></span></div>
  <h5 class="abs f-head" style="left:849px;top:2953px">Payment Method</h5>
  <div class="abs pays"><span class="pay" style="background:#fff"></span><span class="pay" style="background:#1a4fd6"></span><span class="pay" style="background:#222"></span><span class="pay" style="background:#fff"></span></div>
  <div class="abs f-rule"></div>
  <p class="abs copy">© COPYRIGHT 2021 - ALL RIGHTS RESERVED</p>
  <div class="abs top-btn"><svg width="12" height="14" viewBox="0 0 12 14" fill="none" stroke="#fff" stroke-width="1.5"><path d="M6 13V1M1 6l5-5 5 5"/></svg></div>
</footer>

</body>
</html>
```